Business Card Design

I need a business card design for a new business based in South West Australia.
I specialize in residential window cleaning & general handyman maintenance.

Industry/Entity Type

Business

Contact Information for Business Card

Dale Marsh - 512 SILVER HAWK DETAILING
- Window Cleaning
- House Maintenance

```html
<!DOCTYPE html>
<html lang="en">
<head>
<meta charset="utf-8">
<title>Silver Hawk Detailing – Business Card</title>
<link href="https://fonts.googleapis.com/css2?family=Open+Sans:wght@500;600;700&display=swap" rel="stylesheet">
<style>
  :root {
    --page-bg: #e9ecef;
    --card-white: #ffffff;
    --brand-blue: #0a5dac;
    --sky-blue: #0a88cf;
    --accent-gold: #f2c500;
    --ink-white: #ffffff;
  }
  * { box-sizing: border-box; margin: 0; padding: 0; }
  html, body {
    width: 1200px; height: 1200px; overflow: hidden;
    background: var(--page-bg);
    font-family: "Open Sans", Arial, sans-serif;
  }
  .card {
    position: absolute; left: 75px; top: 300px;
    width: 1050px; height: 600px;
    background: var(--card-white);
    box-shadow: 0 10px 30px rgba(0,0,0,0.18);
    overflow: hidden;
  }
  .card-shapes { position: absolute; inset: 0; }
  .brand {
    position: absolute; left: 120px; top: 170px; width: 300px;
    display: flex; align-items: center; gap: 18px;
  }
  .brand-mark { width: 34px; height: 34px; background: var(--accent-gold); flex: none; }
  .brand-name {
    color: var(--brand-blue); font-weight: 700; font-size: 30px; line-height: 1.15;
  }
  .services { position: absolute; left: 120px; top: 400px; width: 325px; list-style: none; }
  .service {
    display: flex; align-items: center; gap: 16px;
    color: var(--sky-blue); font-weight: 600; font-size: 27px;
    padding: 10px 0;
  }
  .service + .service { border-top: 4px solid var(--sky-blue); }
  .service svg { width: 28px; height: 28px; fill: var(--sky-blue); flex: none; }
  .contact-head {
    position: absolute; right: 75px; top: 145px; text-align: right; color: var(--ink-white);
  }
  .person-name { font-weight: 700; font-size: 56px; line-height: 1.1; }
  .phone { font-weight: 600; font-size: 38px; display: flex; align-items: center; justify-content: flex-end; gap: 12px; }
  .phone svg { width: 26px; height: 30px; fill: var(--ink-white); }
  .contact-lines { position: absolute; left: 610px; top: 325px; list-style: none; color: var(--ink-white); }
  .contact-line { display: flex; align-items: center; gap: 18px; font-weight: 600; font-size: 31px; line-height: 1.7; }
  .contact-line svg { width: 30px; height: 30px; fill: var(--ink-white); flex: none; }
</style>
</head>
<body>
<main class="card">
  <svg class="card-shapes" viewBox="0 0 1050 600" width="1050" height="600" aria-hidden="true">
    <path fill="var(--brand-blue)" d="M525 0 H1050 V430 C880 418 700 450 545 525 Z"/>
    <path fill="var(--sky-blue)" d="M560 600 C700 500 860 450 1050 446 V600 Z"/>
  </svg>

  <div class="brand">
    <span class="brand-mark"></span>
    <p class="brand-name">512 SILVER HAWK<br>DETAILING</p>
  </div>

  <ul class="services">
    <li class="service">
      <svg viewBox="0 0 24 24"><path d="M12 2 1 12h3v10h6v-6h4v6h6V12h3z"/></svg>
      Window Cleaning
    </li>
    <li class="service">
      <svg viewBox="0 0 24 24"><path d="M12 2 1 12h3v10h6v-6h4v6h6V12h3z"/></svg>
      House Maintenance
    </li>
  </ul>

  <div class="contact-head">
    <h1 class="person-name">Dale Marsh</h1>
    <p class="phone">
      <svg viewBox="0 0 20 24"><path d="M5 1 1 3c-1 5 3 15 9 19l4-2-3-6-3 1c-2-2-3-5-3-8l3-1z"/></svg>
      041 28 604 77
    </p>
  </div>

  <ul class="contact-lines">
    <li class="contact-line">
      <svg viewBox="0 0 24 24"><path d="M12 2 1 12h3v10h6v-6h4v6h6V12h3z"/></svg>
      #00, Adress 01, Line 02
    </li>
    <li class="contact-line">
      <svg viewBox="0 0 24 24"><path d="M12 2a10 10 0 1 0 0 20 10 10 0 0 0 0-20zm0 2c1 1.3 1.8 3 2.1 5H9.9C10.2 7 11 5.3 12 4zM4.3 13a8 8 0 0 1 0-2h3.6a16 16 0 0 0 0 2zm.7 2h3.1c.3 1.5.8 2.8 1.5 3.8A8 8 0 0 1 5 15zm3.1-6H5a8 8 0 0 1 4.6-3.8C8.9 6.2 8.4 7.5 8.1 9zM12 20c-1-1.3-1.8-3-2.1-5h4.2c-.3 2-1.1 3.7-2.1 5zm2.3-7H9.7a14 14 0 0 1 0-2h4.6a14 14 0 0 1 0 2zm.1 5.8c.7-1 1.2-2.3 1.5-3.8H19a8 8 0 0 1-4.6 3.8zM16.1 13a16 16 0 0 0 0-2h3.6a8 8 0 0 1 0 2zm-.2-4c-.3-1.5-.8-2.8-1.5-3.8A8 8 0 0 1 19 9z"/></svg>
      emailadress@mail.com
    </li>
  </ul>
</main>
</body>
</html>
```